"Nail Care" Postcard

Hello,

We are looking to redesign our current post card. The target audience of this post card age is 50+. We will be mailing these postcards through Tamblo Cards.
The goal of the message is to remind them that it is time to get their (toe) nail care done.

Attached is our previous postcard.
Post card size: 4.2” x 5.5”
Backside of the postcards needs space for the mailing address and postage.
Our address and logo need to be present.
The message of the back of the postcard needs to be present as well.
Examples of stock images must come with the example.
Files preferred to be in TIFF or .ai

Thank you,
Dorian F.

```html
<!DOCTYPE html>
<html lang="en">
<head>
<meta charset="utf-8">
<title>Millbrook Foot &amp; Ankle – Nail Care Postcard</title>
<link rel="stylesheet" href="https://fonts.googleapis.com/css2?family=Jost:wght@400;500;700;800&family=Nunito:wght@800;900&display=swap">
<style>
:root{
  --orange:#e96a32;
  --black:#111111;
  --white:#ffffff;
  --green:#c3dd7a;
  --teal:#3fb58c;
  --canvas:#e4e4e2;
  --navy:#1f2a3c;
}
*{margin:0;padding:0;box-sizing:border-box}
html,body{width:1200px;height:1041px;overflow:hidden}
body{background:var(--canvas);position:relative;font-family:"Jost",sans-serif;color:var(--black)}
.card{position:absolute;width:600px;height:484px;background:var(--white);overflow:hidden;box-shadow:0 2px 10px rgba(0,0,0,.18)}
.card--front{left:300px;top:20px}
.card--back{left:300px;top:537px}
.abs{position:absolute}

/* front */
.front__column{left:377px;top:0;width:223px;height:484px;background:var(--orange)}
.front__base{left:0;top:403px;width:377px;height:81px;background:var(--orange)}
.front__band{left:0;top:26px;width:600px;height:63px;background:var(--black)}
.front__band-rule{left:0;top:89px;width:600px;height:5px;background:var(--green)}
.brand-name{left:40px;top:33px;width:300px;text-align:center;color:var(--orange);font-weight:800;font-size:24px;line-height:23px;letter-spacing:.5px}
.band-address{left:430px;top:36px;color:var(--white);font-size:11.5px;line-height:14px;font-weight:400}
.band-pin{left:379px;top:34px;width:44px;height:48px}
.front__site{left:60px;top:97px;width:264px;text-align:center;font-weight:800;font-size:17px;line-height:20px}
.front__site span{color:var(--orange)}
.headline{font-weight:800;font-size:84px;line-height:1;letter-spacing:-1px;white-space:nowrap}
.headline--time{left:24px;top:144px;color:var(--orange)}
.headline--nail{left:66px;top:220px;color:var(--black)}
.headline--care{left:388px;top:220px;color:var(--white)}
.photo{display:block}
.photo--toes{left:393px;top:112px;width:189px;height:105px;background:linear-gradient(90deg,#e9dcd2,#d9a98c 30%,#ecebe8 50%,#d9a98c 70%,#e9dcd2)}
.photo--exam{left:392px;top:299px;width:192px;height:128px;background:linear-gradient(135deg,#f3f1ee,#e8c1a6 55%,#f6f4f1)}
.photo--team{left:22px;top:306px;width:355px;height:178px;background:linear-gradient(180deg,#3a4457,var(--navy) 70%)}
.front__phone{left:391px;top:443px;color:var(--white);font-weight:700;font-size:20px;line-height:26px;display:flex;align-items:center;gap:10px}

/* back */
.back__brand-name{left:23px;top:50px;width:170px;color:var(--black);font-weight:700;font-size:23px;line-height:26px}
.back__pin{left:208px;top:50px;width:38px;height:42px}
.back__address{left:250px;top:51px;font-size:10.5px;line-height:12.5px}
.back__site{left:23px;top:112px;width:166px;text-align:center;color:var(--orange);font-weight:800;font-size:10px;font-family:"Nunito",sans-serif}
.back__message{left:23px;top:142px;font-family:"Nunito",sans-serif;font-weight:900;font-size:28.5px;line-height:33px;white-space:nowrap}
.back__message .accent{color:var(--orange)}
.back__cta{left:0;top:288px;width:285px;height:61px;background:var(--orange);color:var(--white);font-size:18.5px;line-height:22px;padding:9px 0 0 21px;letter-spacing:.2px;white-space:nowrap}
.back__fold{left:228px;top:349px;width:57px;height:34px}
.back__phone{left:24px;top:363px;display:flex;align-items:center;gap:10px;font-weight:700;font-size:20px;line-height:26px}
.back__note{left:22px;top:401px;font-size:11px;line-height:13.5px;font-weight:400}
.back__recipient{left:334px;top:288px;font-size:16.5px;line-height:19px;font-weight:400;white-space:nowrap}
</style>
</head>
<body>

<section class="card card--front" aria-label="Postcard front">
  <div class="abs front__column"></div>
  <div class="abs front__base"></div>
  <div class="abs front__band"></div>
  <div class="abs front__band-rule"></div>
  <div class="abs brand-name">MILLBROOK<br>FOOT &amp; ANKLE</div>
  <svg class="abs band-pin" viewBox="0 0 44 48" aria-hidden="true">
    <path d="M4 26 L14 22 L22 28 L30 22 L40 26 L40 46 L4 46 Z" fill="none" stroke="#fff" stroke-width="2.5" stroke-linejoin="round"/>
    <path d="M6 44 L38 30 M10 34 L36 44" stroke="#fff" stroke-width="2.2"/>
    <path d="M22 2 a10 10 0 0 1 10 10 c0 8 -10 18 -10 18 s-10 -10 -10 -18 a10 10 0 0 1 10 -10z" fill="#3fb58c"/>
    <path d="M22 7 v10 M17 12 h10" stroke="#fff" stroke-width="2.2"/>
  </svg>
  <div class="abs band-address">58 Harlow Creek Rd.<br>Ste 210<br>Brenton, MD 21900</div>
  <div class="abs front__site">step<span>well</span>feet.com</div>

  <div class="abs headline headline--time">It's t!me</div>
  <div class="abs headline headline--nail">for nail</div>
  <div class="abs headline headline--care">care!</div>

  <div class="abs photo photo--toes" role="img" aria-label="Photo of toes before and after nail treatment"></div>
  <div class="abs photo photo--exam" role="img" aria-label="Photo of a podiatrist examining a patient's foot"></div>
  <div class="abs photo photo--team" role="img" aria-label="Group photo of the clinic's care team in dark scrubs"></div>

  <div class="abs front__phone">
    <svg width="32" height="32" viewBox="0 0 32 32" aria-hidden="true">
      <path d="M6 6 c-3 3 -2 9 4 15 s12 7 15 4 l-4 -5 l-4 2 c-3 -1 -6 -4 -7 -7 l2 -4 z" fill="none" stroke="#fff" stroke-width="2" stroke-linejoin="round"/>
      <circle cx="24" cy="8" r="7" fill="#3fb58c"/>
      <circle cx="21" cy="8" r="1" fill="#fff"/><circle cx="24" cy="8" r="1" fill="#fff"/><circle cx="27" cy="8" r="1" fill="#fff"/>
    </svg>
    <span>(555)014-2297</span>
  </div>
</section>

<section class="card card--back" aria-label="Postcard back">
  <div class="abs back__brand-name">Millbrook<br>Foot &amp; Ankle</div>
  <svg class="abs back__pin" viewBox="0 0 44 48" aria-hidden="true">
    <path d="M4 26 L14 22 L22 28 L30 22 L40 26 L40 46 L4 46 Z" fill="none" stroke="#e96a32" stroke-width="2.5" stroke-linejoin="round"/>
    <path d="M6 44 L38 30 M10 34 L36 44" stroke="#e96a32" stroke-width="2.2"/>
    <path d="M22 2 a10 10 0 0 1 10 10 c0 8 -10 18 -10 18 s-10 -10 -10 -18 a10 10 0 0 1 10 -10z" fill="#3fb58c"/>
    <path d="M22 7 v10 M17 12 h10" stroke="#e96a32" stroke-width="2.2"/>
  </svg>
  <div class="abs back__address">58 Harlow Creek Rd.<br>Ste 210<br>Brenton, MD 21900</div>
  <div class="abs back__site">stepwellfeet.com</div>

  <div class="abs back__message">
    <span class="accent">We are pleased to</span><br>
    inform you may be due<br>
    <span class="accent">for your bimonthly</span><br>
    nail care!
  </div>

  <div class="abs back__cta">Please call our office<br>to schedule your appointment.</div>
  <svg class="abs back__fold" viewBox="0 0 57 34" aria-hidden="true"><path d="M0 0 H57 L0 34 Z" fill="#111"/></svg>

  <div class="abs back__phone">
    <svg width="34" height="34" viewBox="0 0 32 32" aria-hidden="true">
      <path d="M6 6 c-3 3 -2 9 4 15 s12 7 15 4 l-4 -5 l-4 2 c-3 -1 -6 -4 -7 -7 l2 -4 z" fill="none" stroke="#111" stroke-width="2" stroke-linejoin="round"/>
      <circle cx="24" cy="8" r="7" fill="#3fb58c"/>
      <circle cx="21" cy="8" r="1" fill="#fff"/><circle cx="24" cy="8" r="1" fill="#fff"/><circle cx="27" cy="8" r="1" fill="#fff"/>
    </svg>
    <span>(555)014-2297</span>
  </div>

  <div class="abs back__note">*If you have received<br>nail care within<br>the past two months,<br>please disregard*</div>

  <div class="abs back__recipient">John Smith<br>123 Main Street<br>Small Town, USA 00000-0000</div>
</section>

</body>
</html>
```